Plumbing business card and logo desgin

Need a new business card and logo for a plumbing business based in Warragul, Australia. Business name is 7Kelby plumbing & air-conditioning. We service all plumbing and gasfitting needs and installation of air-conditioning. We clear blocked drains, install new hot water systems, central heating, new and existing homes, roofing, sanitary and drainage.
i would like to have a space on there for website, email, phone, licence number and what we do as a company.
i would like a water droplet to be incorporated into the design to try and stand out that we are a plumbing business

Contact Information for Business Card

website:
phone number: 0458271936
Licence Number: 382716

Logo Text

7Kelby Plumbing & Air-Conditioning

```html
<!DOCTYPE html>
<html lang="en">
<head>
<meta charset="utf-8">
<title>7Kelby Plumbing &amp; Air-Conditioning – Business Card</title>
<link rel="stylesheet" href="https://fonts.googleapis.com/css2?family=Roboto:wght@400;700;900&display=swap">
<style>
  :root {
    --stage: #b9b9b9;
    --blue-top: #23a8e1;
    --blue-bottom: #1480c4;
    --brand-blue: #1a8fd3;
    --panel-grey: #8e8e8e;
    --text-grey: #8a8a8a;
    --white: #ffffff;
  }
  * { margin: 0; padding: 0; box-sizing: border-box; }
  html, body { width: 1200px; height: 801px; overflow: hidden; }
  body {
    position: relative;
    background: var(--stage);
    font-family: "Roboto", Arial, sans-serif;
  }
  .card {
    position: absolute;
    top: 274px;
    width: 443px;
    height: 263px;
    overflow: hidden;
  }
  /* Front */
  .card--front {
    left: 153px;
    background: linear-gradient(180deg, var(--blue-top), var(--blue-bottom));
    color: var(--white);
  }
  .front__panel {
    position: absolute;
    top: 0; right: 0;
    width: 134px; height: 100%;
    background: var(--panel-grey);
    display: flex; align-items: center; justify-content: center;
  }
  .front__brand {
    font-weight: 900;
    font-size: 22px;
    letter-spacing: 1px;
    color: var(--white);
  }
  .front__name {
    position: absolute; left: 24px; top: 29px;
    font-weight: 900; font-size: 19px; letter-spacing: 0.3px;
  }
  .front__role {
    position: absolute; left: 24px; top: 51px;
    font-size: 11px;
  }
  .front__licence {
    position: absolute; left: 24px; top: 76px;
    font-size: 13px;
  }
  .contact {
    position: absolute; left: 21px; top: 189px;
    list-style: none; font-size: 13px; line-height: 16.8px;
  }
  .contact li { display: flex; align-items: center; gap: 5px; }
  .contact svg { width: 11px; height: 11px; flex: none; }
  /* Back */
  .card--back {
    left: 625px;
    background: var(--white);
  }
  .back__brand {
    position: absolute; left: 26px; top: 42px;
    display: flex; align-items: center; gap: 12px;
  }
  .back__dot {
    width: 26px; height: 26px; border-radius: 50%;
    background: var(--brand-blue);
  }
  .back__name {
    font-weight: 900; font-size: 17px;
    color: var(--brand-blue);
    letter-spacing: 0.2px;
  }
  .services {
    position: absolute; left: 103px; top: 111px;
    list-style: none;
    font-size: 11.5px; line-height: 14.65px;
    color: var(--text-grey);
    text-transform: uppercase;
    letter-spacing: 0.2px;
  }
  .services li { display: flex; align-items: center; gap: 7px; }
  .services li::before {
    content: ""; width: 5px; height: 5px; border-radius: 50%;
    background: var(--brand-blue);
  }
</style>
</head>
<body>
  <section class="card card--front">
    <h1 class="front__name">RYAN KELBY</h1>
    <p class="front__role">DIRECTOR</p>
    <p class="front__licence">LIC NO: 382716</p>
    <ul class="contact">
      <li>
        <svg viewBox="0 0 12 12"><path d="M2.5 1 4.5 3.2 3.4 4.6c.8 1.7 2.2 3.1 4 4l1.4-1.1L11 9.5 9.8 11C5.2 10.5 1.5 6.8 1 2.2Z" fill="none" stroke="#fff" stroke-width="1.2"/></svg>
        0458271936
      </li>
      <li>
        <svg viewBox="0 0 12 12"><rect x="0.6" y="2.2" width="10.8" height="7.6" fill="none" stroke="#fff" stroke-width="1.2"/><path d="M0.6 2.2 6 6.6l5.4-4.4" fill="none" stroke="#fff" stroke-width="1.2"/></svg>
        info@7kelbyplumbing.com
      </li>
      <li>
        <svg viewBox="0 0 12 12" fill="none" stroke="#fff" stroke-width="1"><circle cx="6" cy="6" r="5.2"/><ellipse cx="6" cy="6" rx="2.3" ry="5.2"/><path d="M0.8 6h10.4M1.6 3.4h8.8M1.6 8.6h8.8"/></svg>
        www.7kelbyplumbing.com
      </li>
    </ul>
    <div class="front__panel">
      <span class="front__brand">7KELBY</span>
    </div>
  </section>

  <section class="card card--back">
    <div class="back__brand">
      <span class="back__dot"></span>
      <span class="back__name">7Kelby Plumbing &amp; Air-Conditioning</span>
    </div>
    <ul class="services">
      <li>All plumbing</li>
      <li>Gasfitting</li>
      <li>Installation of air-conditioning</li>
      <li>Clear blocked drains</li>
      <li>Install new hot water systems</li>
      <li>Central heating</li>
      <li>New and existing homes</li>
      <li>Roofing</li>
      <li>Sanitary and drainage</li>
    </ul>
  </section>
</body>
</html>
```